Tiko Marsden Systems Web Site

I need website designed for Tiko Marsden Systems, LLC. It is an email marketing software as a service business. I am looking for a five page website with the ability to accept payments. I have included our logo below for integration with the website. I do not have the text ready yet.

The domain to use is tiko-marsden.example

I have also included some examples of other websites that outline the basic structure I would like
https://trybluvoren.example/
https://www.postquill.example/

I know I need to provide some more information, but I want to get the ball rolling and see what is needed.
Thanks!
Owen

```html
<!DOCTYPE html>
<html lang="en">
<head>
<meta charset="utf-8">
<title>Tiko Marsden Systems</title>
<link href="https://fonts.googleapis.com/css2?family=Lato:wght@400;700;900&display=swap" rel="stylesheet">
<style>
:root{
  --red:#d7182a;
  --blue:#3a8fd6;
  --blue-dark:#2f73b8;
  --ink:#1d1d1d;
  --text:#555;
  --muted:#888;
  --line:#d9d9d9;
  --soft:#f2f2f2;
  --footer:#1c1c1c;
  --white:#fff;
}
*{box-sizing:border-box;margin:0;padding:0}
html,body{width:1200px;height:4569px;overflow:hidden}
body{font-family:"Lato",Arial,sans-serif;color:var(--ink);background:var(--white);position:relative}
.abs{position:absolute}
a{color:inherit;text-decoration:none}

/* header */
.site-header{position:absolute;top:0;left:0;width:1200px;height:95px;background:var(--white);z-index:5}
.brand-badge{position:absolute;left:80px;top:-40px;width:224px;height:224px;border-radius:50%;background:var(--white);z-index:6;display:flex;flex-direction:column;align-items:center;justify-content:center;text-align:center}
.brand-dot{width:54px;height:54px;border-radius:50%;border:3px solid var(--red);margin:26px 0 12px}
.brand-name{font-weight:900;font-size:21px;color:var(--ink);letter-spacing:1px;line-height:1.15}
.brand-url{font-size:10px;color:var(--blue-dark);margin-top:6px;font-weight:700}
.main-nav{position:absolute;left:405px;top:36px;display:flex;gap:30px;font-size:15px;font-weight:700;color:var(--ink)}
.search-icon{position:absolute;left:930px;top:36px}
.login-btn{position:absolute;left:987px;top:24px;width:115px;height:44px;border:2px solid var(--red);border-radius:22px;color:var(--red);font-weight:700;font-size:15px;display:flex;align-items:center;justify-content:center;gap:6px}

/* hero */
.hero{position:absolute;top:95px;left:0;width:1200px;height:510px;background:linear-gradient(120deg,#4a87c4 0%,#6aa3d8 45%,#8bbbe4 100%)}
.hero-title{position:absolute;top:70px;width:100%;text-align:center;color:var(--white);font-weight:900;font-size:70px;letter-spacing:2px}
.hero-sub{position:absolute;top:158px;width:100%;text-align:center;color:var(--white);font-weight:700;font-size:26px}
.hero-btn{position:absolute;left:494px;top:222px;width:213px;height:55px;border:2px solid var(--white);border-radius:28px;color:var(--white);font-weight:700;font-size:15px;display:flex;align-items:center;justify-content:center;letter-spacing:1px}
.hero-device{position:absolute;left:369px;top:433px;width:463px;height:319px;border-radius:14px;background:#1e1e1e;padding:18px;z-index:3}
.hero-device .screen{width:100%;height:100%;background:linear-gradient(180deg,#e9eef5,#ffffff)}

/* trusted */
.section-title{position:absolute;width:100%;text-align:center;font-weight:900;color:var(--ink)}
.trusted-title{top:815px;font-size:27px;font-weight:700}
.logo-box{position:absolute;top:893px;width:186px;height:88px;border:1px solid var(--line);display:flex;align-items:center;justify-content:center;font-size:19px;font-weight:700;color:#555}
.round-arrow{position:absolute;width:38px;height:38px;border:1.5px solid #999;border-radius:50%;display:flex;align-items:center;justify-content:center}
.divider{position:absolute;left:97px;top:1042px;width:1006px;height:1px;background:#ccc}

/* welcome */
.welcome-title{top:1145px;font-size:38px}
.welcome-text{position:absolute;left:183px;top:1222px;width:834px;text-align:center;font-size:14px;line-height:24px;color:var(--text)}
.feature{position:absolute;top:1316px;width:340px;text-align:center}
.feature h3{font-size:23px;font-weight:700;margin-top:10px}
.feature p{font-size:14px;line-height:21px;color:var(--text);margin:14px auto 0;width:290px}
.read-more{display:block;color:var(--red);font-weight:900;font-size:14px;margin-top:20px}
.feature-icon{width:220px;height:220px;margin:10px auto 0;border-radius:50%;border:4px solid var(--blue);display:flex;align-items:center;justify-content:center}

/* why */
.why-photo{position:absolute;left:0;top:1834px;width:600px;height:466px;background:linear-gradient(135deg,#caa36a 0%,#8a7a6a 50%,#5b5e66 100%)}
.why-box{position:absolute;left:600px;top:1864px;width:500px;height:406px;border:2px solid var(--line);border-left:none;background:var(--white)}
.why-box h2{position:absolute;left:50px;top:38px;font-size:32px;font-weight:900}
.why-item{position:absolute;left:50px;display:flex;gap:20px;align-items:center}
.why-icon{width:74px;height:74px;border-radius:50%;flex:none;display:flex;align-items:center;justify-content:center}
.why-item h4{font-size:19px;font-weight:400;color:var(--ink)}
.why-item p{font-size:13px;color:var(--text);margin-top:6px}

/* blog */
.blog{position:absolute;left:0;top:2412px;width:1200px;height:978px;background:var(--soft)}
.blog-title{top:82px;font-size:36px}
.card{position:absolute;background:var(--white);border:1px solid #e3e3e3}
.card .thumb{width:100%}
.card h3{font-size:19px;font-weight:400;line-height:27px;color:var(--ink);padding:0 22px;margin-top:18px}
.meta{display:flex;align-items:center;gap:8px;font-size:13px;color:#666;padding:0 22px;margin-top:10px}
.meta .bar{color:#aaa;margin:0 6px}
.view-more{position:absolute;left:515px;top:817px;width:167px;height:61px;border-radius:31px;background:var(--red);color:var(--white);font-weight:900;font-size:16px;display:flex;align-items:center;justify-content:center}

/* cta */
.cta{position:absolute;left:0;top:3390px;width:1200px;height:311px;background:var(--blue)}
.cta h2{position:absolute;top:56px;width:100%;text-align:center;color:var(--white);font-size:38px;font-weight:700;line-height:52px}
.cta-btn{position:absolute;left:487px;top:180px;width:226px;height:64px;border:2px solid var(--white);border-radius:32px;color:var(--white);font-weight:700;font-size:19px;display:flex;align-items:center;justify-content:center;letter-spacing:1px}

/* testimonial */
.quote-text{position:absolute;left:183px;top:3932px;width:834px;text-align:center;font-style:italic;font-size:14px;line-height:27px;color:#666}
.quote-author{position:absolute;top:4056px;width:100%;text-align:center;font-size:16px;color:#333}

/* footer */
.site-footer{position:absolute;left:0;top:4167px;width:1200px;height:402px;background:var(--footer);color:#ccc}
.footer-brand{position:absolute;left:91px;top:40px;width:274px;text-align:center;color:var(--white)}
.footer-brand .brand-dot{border-color:var(--white);margin:0 auto 18px;width:70px;height:70px}
.footer-brand .name{font-size:26px;font-weight:900;letter-spacing:1px}
.footer-brand .url{font-size:13px;margin-top:18px;letter-spacing:1px}
.footer-col{position:absolute;top:90px}
.footer-col h4{font-size:19px;font-weight:700;color:var(--white);margin-bottom:20px}
.footer-col li{list-style:none;font-size:13px;line-height:24px}
.news-input{width:255px;height:36px;border:1px solid #888;background:var(--white);color:#888;font-size:12px;padding:10px;margin-top:16px}
.subscribe{width:108px;height:34px;border-radius:17px;background:var(--red);color:var(--white);font-weight:900;font-size:12px;display:flex;align-items:center;justify-content:center;margin-top:18px}
.contact-line{display:flex;gap:20px;font-size:13px;line-height:20px;margin-bottom:18px}
.footer-rule{position:absolute;left:91px;top:316px;width:1010px;height:1px;background:#444}
.copyright{position:absolute;left:100px;top:340px;font-size:12px}
.social{position:absolute;left:978px;top:330px;display:flex;gap:10px}
.social span{width:22px;height:22px;border-radius:50%;border:1px solid #aaa;display:block}
</style>
</head>
<body>

<header class="site-header">
  <nav class="main-nav">
    <a href="#">ABOUT US</a><a href="#">SOLUTIONS</a><a href="#">PRICING</a><a href="#">BLOG</a><a href="#">CONTACT US</a>
  </nav>
  <svg class="search-icon" width="18" height="18" viewBox="0 0 18 18"><circle cx="7" cy="7" r="5.5" fill="none" stroke="#1d1d1d" stroke-width="2.2"/><line x1="11" y1="11" x2="16" y2="16" stroke="#1d1d1d" stroke-width="2.4"/></svg>
  <a class="login-btn" href="#"><svg width="11" height="13" viewBox="0 0 11 13"><rect x="0" y="5" width="11" height="8" rx="1" fill="#d7182a"/><path d="M2.5 5V3.5a3 3 0 0 1 6 0V5" fill="none" stroke="#d7182a" stroke-width="1.8"/></svg>LOGIN</a>
</header>
<div class="brand-badge">
  <div class="brand-dot"></div>
  <div class="brand-name">TIKO MARSDEN<br>SYSTEMS</div>
  <div class="brand-url">www.tiko-marsden.example</div>
</div>

<section class="hero" role="img" aria-label="Blue-tinted photo of a laptop on a desk showing email marketing">
  <h1 class="hero-title">TIKO MARSDEN</h1>
  <p class="hero-sub">We are an email marketing software as a service business</p>
  <a class="hero-btn" href="#">SIGN UP FOR FREE</a>
</section>
<div class="hero-device"><div class="screen" role="img" aria-label="Tablet showing the email dashboard with recipient activity"></div></div>

<h2 class="section-title trusted-title">TRUSTED BY TEAMS EVERYWHERE</h2>
<div class="round-arrow" style="left:36px;top:918px"><svg width="10" height="14" viewBox="0 0 10 14"><path d="M8 1 2 7l6 6" fill="none" stroke="#777" stroke-width="2"/></svg></div>
<div class="logo-box" style="left:97px">Northfield Daily</div>
<div class="logo-box" style="left:304px">Orbit News</div>
<div class="logo-box" style="left:509px">Venture Weekly</div>
<div class="logo-box" style="left:713px">Kestrel TV</div>
<div class="logo-box" style="left:917px">The Harbor Times</div>
<div class="round-arrow" style="left:1126px;top:918px"><svg width="10" height="14" viewBox="0 0 10 14"><path d="M2 1l6 6-6 6" fill="none" stroke="#777" stroke-width="2"/></svg></div>
<div class="divider"></div>

<h2 class="section-title welcome-title">WELCOME TO TIKO MARSDEN</h2>
<p class="welcome-text">At vero eos et accusamus et iusto odio dignissimos ducimus qui blanditiis praesentium voluptatum deleniti atque corrupti quos dolores et quas molestias excepturi sint occaecati cupiditate non provident, similique sunt in culpa qui officia des.</p>

<div class="feature" style="left:77px">
  <div class="feature-icon"><svg width="52" height="36" viewBox="0 0 52 36"><rect width="52" height="36" fill="#d7182a"/><path d="M0 0l26 20L52 0" fill="none" stroke="#fff" stroke-width="3"/></svg></div>
  <h3>Personalize your emails</h3>
  <p>Nam libero tempore, cum soluta nobis est eligendi optio cumque nihil impedit quo minus id quod maxime placeat facere</p>
  <a class="read-more" href="#">READ MORE</a>
</div>
<div class="feature" style="left:430px">
  <div class="feature-icon"><svg width="72" height="44" viewBox="0 0 72 44"><circle cx="36" cy="10" r="10" fill="#d7182a"/><circle cx="14" cy="16" r="8" fill="#d7182a"/><circle cx="58" cy="16" r="8" fill="#d7182a"/><path d="M20 44a16 16 0 0 1 32 0zM0 42a14 14 0 0 1 24-6v6zM72 42a14 14 0 0 0-24-6v6z" fill="#d7182a"/></svg></div>
  <h3>Team collaboration</h3>
  <p>Nam libero tempore, cum soluta nobis est eligendi optio cumque nihil impedit quo minus id quod maxime placeat facere</p>
  <a class="read-more" href="#">READ MORE</a>
</div>
<div class="feature" style="left:783px">
  <div class="feature-icon"><svg width="54" height="54" viewBox="0 0 54 54"><circle cx="22" cy="22" r="16" fill="none" stroke="#d7182a" stroke-width="7"/><line x1="34" y1="34" x2="50" y2="50" stroke="#d7182a" stroke-width="9" stroke-linecap="round"/></svg></div>
  <h3>A/B testing</h3>
  <p>Nam libero tempore, cum soluta nobis est eligendi optio cumque nihil impedit quo minus id quod maxime placeat facere</p>
  <a class="read-more" href="#">READ MORE</a>
</div>

<div class="why-photo" role="img" aria-label="Photo of hands holding a smartphone with message icons floating above it"></div>
<section class="why-box">
  <h2>WHY CHOOSE US</h2>
  <div class="why-item" style="top:106px">
    <div class="why-icon" style="background:var(--blue)"><svg width="34" height="30" viewBox="0 0 34 30"><rect x="1" y="1" width="32" height="21" rx="2" fill="none" stroke="#fff" stroke-width="3"/><rect x="12" y="24" width="10" height="5" fill="#fff"/></svg></div>
    <div><h4>Powerful APIs</h4><p>At vero eos et accusamus et iusto odio dignissimos</p></div>
  </div>
  <div class="why-item" style="top:203px">
    <div class="why-icon" style="border:2px solid #e3e3e3"><svg width="32" height="24" viewBox="0 0 32 24"><rect width="32" height="24" rx="2" fill="#3a8fd6"/><path d="M1 2l15 12L31 2" fill="none" stroke="#fff" stroke-width="2.5"/></svg></div>
    <div><h4>SMTP Relay</h4><p>At vero eos et accusamus et iusto odio dignissimos</p></div>
  </div>
  <div class="why-item" style="top:298px">
    <div class="why-icon" style="border:2px solid #e3e3e3"><svg width="32" height="26" viewBox="0 0 32 26"><path d="M2 7h26M22 1l6 6-6 6M30 19H4M10 13l-6 6 6 6" fill="none" stroke="#3a8fd6" stroke-width="3"/></svg></div>
    <div><h4>Transactional SMS</h4><p>At vero eos et accusamus et iusto odio dignissimos</p></div>
  </div>
</section>

<section class="blog">
  <h2 class="section-title blog-title">OUR BLOG</h2>
  <article class="card" style="left:97px;top:177px;width:567px;height:588px">
    <div class="thumb" role="img" aria-label="Photo of a person arranging app sticky notes on a glass board" style="height:457px;background:linear-gradient(135deg,#e8e4de,#b7c7cf 60%,#8a9aa6)"></div>
    <h3>At vero eos et accusamus et iusto odio dignissimos ducimus qui blanditiis praesentium</h3>
    <div class="meta"><svg width="12" height="12" viewBox="0 0 12 12"><rect y="2" width="12" height="10" fill="#3a8fd6"/></svg>22/09/2018<span class="bar">|</span><svg width="12" height="12" viewBox="0 0 12 12"><circle cx="6" cy="3.5" r="3" fill="#3a8fd6"/><path d="M0 12a6 6 0 0 1 12 0z" fill="#3a8fd6"/></svg>John Doe</div>
  </article>
  <article class="card" style="left:704px;top:177px;width:396px;height:277px">
    <div class="thumb" role="img" aria-label="Photo of a business team meeting around a laptop" style="height:168px;background:linear-gradient(135deg,#d9dde2,#8c97a3)"></div>
    <h3>At vero eos et accusamus et iustodio dignissimos ducimus qui.</h3>
    <div class="meta"><svg width="12" height="12" viewBox="0 0 12 12"><rect y="2" width="12" height="10" fill="#3a8fd6"/></svg>22/09/2018<span class="bar">|</span><svg width="12" height="12" viewBox="0 0 12 12"><circle cx="6" cy="3.5" r="3" fill="#3a8fd6"/><path d="M0 12a6 6 0 0 1 12 0z" fill="#3a8fd6"/></svg>John Doe</div>
  </article>
  <article class="card" style="left:704px;top:488px;width:396px;height:277px">
    <div class="thumb" role="img" aria-label="Illustration of social notification counters on a blue screen" style="height:170px;background:linear-gradient(135deg,#4c6bd0,#3047a6)"></div>
    <h3>At vero eos et accusamus et iustodio dignissimos ducimus qui.</h3>
    <div class="meta"><svg width="12" height="12" viewBox="0 0 12 12"><rect y="2" width="12" height="10" fill="#3a8fd6"/></svg>22/09/2018<span class="bar">|</span><svg width="12" height="12" viewBox="0 0 12 12"><circle cx="6" cy="3.5" r="3" fill="#3a8fd6"/><path d="M0 12a6 6 0 0 1 12 0z" fill="#3a8fd6"/></svg>John Doe</div>
  </article>
  <a class="view-more" href="#">VIEW MORE</a>
</section>

<section class="cta">
  <h2>100,000 companies use Tiko Marsden daily.<br>You too can send better emails.</h2>
  <a class="cta-btn" href="#">JOIN US TODAY</a>
</section>

<svg class="abs" style="left:545px;top:3808px" width="110" height="86" viewBox="0 0 110 86"><path d="M0 86V48C0 20 14 4 42 0v14C28 18 22 28 22 40h22v46zM62 86V48C62 20 76 4 104 0v14C90 18 84 28 84 40h22v46z" fill="#d7182a"/></svg>
<svg class="abs" style="left:88px;top:3960px" width="20" height="32" viewBox="0 0 20 32"><path d="M17 2 3 16l14 14" fill="none" stroke="#666" stroke-width="3"/></svg>
<svg class="abs" style="left:1092px;top:3960px" width="20" height="32" viewBox="0 0 20 32"><path d="M3 2l14 14L3 30" fill="none" stroke="#666" stroke-width="3"/></svg>
<p class="quote-text">" Lorem ipsum dolor sit amet, consectetur adipiscing elit, sed do eiusmod tempor incididunt ut labore et dolore magna aliqua. Ut enim ad minim veniam, quis nostrud exercitation ullamco laboris nisi ut aliquip ex ea commodo consequat. Duis aute irure dolor in reprehenderit in voluptate velit esse cillum dolore eu fugiat nulla pariatur "</p>
<p class="quote-author">- JOHN DOE</p>

<footer class="site-footer">
  <div class="footer-brand">
    <div class="brand-dot"></div>
    <div class="name">TIKO MARSDEN<br>SYSTEMS</div>
    <div class="url">www.tiko-marsden.example</div>
  </div>
  <div class="footer-col" style="left:430px">
    <h4>Quick Links</h4>
    <ul><li>Help</li><li>FAQ</li><li>Support</li><li>Sitemap</li><li>Terms Of Use</li><li>Privacy Statement</li></ul>
  </div>
  <div class="footer-col" style="left:609px">
    <h4>Newsletter Subscription</h4>
    <p style="font-size:13px;line-height:19px;width:230px">Register your Email Address to get information about us</p>
    <div class="news-input">Email Address</div>
    <div class="subscribe">SUBSCRIBE</div>
  </div>
  <div class="footer-col" style="left:920px">
    <h4>Contact Us</h4>
    <div class="contact-line"><svg width="12" height="16" viewBox="0 0 12 16"><path d="M6 0a6 6 0 0 1 6 6c0 4-6 10-6 10S0 10 0 6a6 6 0 0 1 6-6z" fill="#fff"/><circle cx="6" cy="6" r="2" fill="#1c1c1c"/></svg><span>Lindenweg 14<br>4100 Arvelund</span></div>
    <div class="contact-line"><svg width="14" height="14" viewBox="0 0 14 14"><path d="M3 0l3 3-2 2c1 2 3 4 5 5l2-2 3 3-2 3C6 14 0 8 0 3z" fill="#fff"/></svg><span>1 555 010 0199</span></div>
    <div class="contact-line"><svg width="14" height="11" viewBox="0 0 14 11"><rect width="14" height="11" fill="#fff"/><path d="M0 1l7 5 7-5" fill="none" stroke="#1c1c1c" stroke-width="1.5"/></svg><span>info@tiko-marsden.example</span></div>
  </div>
  <div class="footer-rule"></div>
  <p class="copyright">Copyrights © 2018, Tiko Marsden. All rights reserved.</p>
  <div class="social"><span></span><span></span><span></span><span></span></div>
</footer>

</body>
</html>
```